Mi ZOV Menu

I am attaching our menu itmes for our new fast casual business. I need to design a printable menu. Tri fold or bi fold depending on what fits. I want it to be easy to order but also look cool. If we can get a general design and I can add pictures if needed when I get them. For now they can be generic

Industry/Entity Type

Food

Font styles to use
Serif

Colors
0054AA
0677BA
7BADD7
CADEEF
E8F1F8

Requirements
Nice to have
• Some other businesses that have similar menus are redmaplediner.com and thelanternworks.com https://pelmorahouse.ca/en/food-menu/

```html
<!DOCTYPE html>
<html lang="en">
<head>
<meta charset="utf-8">
<title>Mi ZOV Food Menu</title>
<link rel="stylesheet" href="https://fonts.googleapis.com/css2?family=Oswald:wght@500;700&family=Montserrat:wght@400;600;700&family=Anton&display=swap">
<style>
:root{
  --blue:#0054AA;
  --blue-mid:#0677BA;
  --blue-soft:#7BADD7;
  --blue-pale:#CADEEF;
  --blue-mist:#E8F1F8;
  --gold:#f5a519;
  --gold-deep:#eea011;
  --paper:#eef3f8;
  --paper-light:#f7f9fc;
  --ink:#14233f;
  --muted:#4f5d75;
  --stage:#e3e3e3;
}
*{margin:0;padding:0;box-sizing:border-box}
html,body{width:1200px;height:2475px;overflow:hidden;background:var(--stage)}
body{position:relative;font-family:'Montserrat',sans-serif}
.spread{position:absolute;left:170px;width:909px;height:702px;box-shadow:0 6px 18px rgba(0,0,0,.12);overflow:hidden}
.spread-cover{top:953px}
.spread-inside{top:1742px;height:703px}
.panel{position:absolute;top:0;height:100%;width:454px}
.panel-left{left:0}
.panel-right{left:454px;width:455px}
.navy{background:var(--blue);color:#fff}
.gold{background:var(--gold)}
.paper{background:linear-gradient(180deg,var(--paper-light),var(--paper))}
.abs{position:absolute}
.heading{font-family:'Oswald',sans-serif;font-weight:700;font-size:18px;letter-spacing:.2px;display:flex;align-items:center;gap:6px;white-space:nowrap;z-index:2}
.heading::after{content:"";display:block;height:0;border-bottom:1px dotted currentColor;opacity:.7;width:var(--rule,160px);margin-top:8px}
.on-navy .heading{color:var(--gold)}
.on-gold .heading,.on-paper .heading{color:var(--blue)}
.item{position:absolute;display:flex;justify-content:space-between;align-items:flex-start;z-index:2}
.item .name{font-weight:700;font-size:10.5px;line-height:1.25;text-transform:uppercase;white-space:nowrap}
.item .price{font-weight:700;font-size:10.5px;white-space:nowrap}
.item .note{display:block;font-weight:400;font-size:7.5px;line-height:1.25;margin-top:2px;text-transform:none;white-space:nowrap}
.caps .note{text-transform:uppercase}
.on-navy .name,.on-navy .price,.on-navy .note{color:#fff}
.on-gold .name,.on-gold .price,.on-gold .note{color:#fff}
.on-paper .name,.on-paper .price{color:var(--ink)}
.on-paper .note{color:var(--muted)}
.desc{font-size:8px;line-height:1.3;text-transform:uppercase;white-space:nowrap;letter-spacing:-.2px;z-index:2}
.photo{position:absolute;border-radius:8px;z-index:1}
.decor{position:absolute;opacity:.25}

.burger-title{left:0;width:454px;top:24px;text-align:center;font-family:'Oswald',sans-serif;font-weight:700;color:var(--gold);font-size:25px;line-height:1}
.burger-tag{left:0;width:454px;top:52px;text-align:center;font-family:'Oswald',sans-serif;font-weight:700;font-size:19px;color:#fff}
.burger-desc{left:0;width:454px;top:79px;text-align:center;font-family:'Oswald',sans-serif;font-weight:500;font-size:9.5px;color:#fff}
.brand-name{left:0;width:455px;top:72px;text-align:center;font-family:'Anton',sans-serif;color:var(--gold);font-size:64px;line-height:1;letter-spacing:1px}
.word-food{left:0;width:455px;top:150px;text-align:center;font-family:'Anton',sans-serif;color:var(--blue);font-size:124px;line-height:1;letter-spacing:2px}
.word-menu{left:0;width:455px;top:272px;text-align:center;font-family:'Anton',sans-serif;color:var(--gold);font-size:124px;line-height:1;letter-spacing:2px}
.site{left:0;width:455px;top:641px;display:flex;align-items:center;justify-content:center;gap:8px;font-weight:700;font-size:12px;color:var(--blue);letter-spacing:.6px}
.site::before,.site::after{content:"";width:80px;border-top:1px solid var(--blue-soft)}
.gold-strip{position:absolute;left:359px;top:0;width:96px;height:100%;background:var(--gold)}
</style>
</head>
<body>

<section class="spread spread-cover">
  <div class="panel panel-left navy on-navy">
    <div class="decor" style="left:350px;top:0;width:104px;height:90px;background:var(--blue-soft)" role="img" aria-label="Line-drawn olive branch ornament"></div>
    <div class="decor" style="left:0;top:600px;width:90px;height:102px;background:var(--blue-soft)" role="img" aria-label="Line-drawn olive branch ornament"></div>
    <div class="abs burger-title">MI ZOV'S GREEK MAFIA BURGER</div>
    <div class="abs burger-tag">"IT'S TO DIE FOR"</div>
    <div class="abs burger-desc">EGG, GRILLED ONION, CHEDDAR, TOMATOES, PICKLED JALAPENOS &amp; ZOV MAFIA SAUCE</div>

    <div class="abs heading" style="left:27px;top:122px;--rule:165px">MI ZOV KIDS</div>
    <div class="item caps" style="left:27px;top:162px;width:325px"><span class="name">MIZOV- Chicken Skewer<span class="note">Served with fried and tzaziki</span></span><span class="price">7</span></div>
    <div class="item caps" style="left:27px;top:207px;width:329px"><span class="name">Mi ZOV- Baked Salmon<span class="note">Served with rice</span></span><span class="price">12</span></div>
    <div class="item caps" style="left:27px;top:252px;width:325px"><span class="name">Mi ZOV-Little Mafia Burger<span class="note">Single burger with little ZOV mafia sauce with fries</span></span><span class="price">8</span></div>

    <div class="abs heading" style="left:27px;top:305px;--rule:160px">SIDES</div>
    <div class="item" style="left:27px;top:340px;width:326px"><span class="name">Mi ZOV- Greek Oven Potatoes</span><span class="price">6</span></div>
    <div class="item" style="left:27px;top:372px;width:328px"><span class="name">Mi ZOV- Rice</span><span class="price">2</span></div>
    <div class="item" style="left:27px;top:403px;width:326px"><span class="name">Mi ZOV- Greek Style Green Beans Baked<br>In Tomato Sauce</span><span class="price" style="margin-top:16px">6</span></div>
    <div class="item" style="left:27px;top:451px;width:328px"><span class="name">Mi ZOV-Pita</span><span class="price">2</span></div>

    <div class="abs heading" style="left:27px;top:493px;--rule:185px">SKEWERS</div>
    <div class="item caps" style="left:27px;top:531px;width:260px"><span class="name">Mi ZOV Chicken Souvlaki Skewers<span class="note">10 skewers 25.00 20 skewers 50.00</span></span></div>
    <div class="item caps" style="left:27px;top:575px;width:260px"><span class="name">Mi ZOV Pork Souvlaki Skewers<span class="note">10 skewers 25.00 20 skewers 50.00</span></span></div>

    <div class="photo" style="left:290px;top:555px;width:155px;height:145px;background:linear-gradient(135deg,#d9a06a,#e9835a 55%,#8fb04d);transform:rotate(-28deg)" role="img" aria-label="Photo of shrimp souvlaki skewers on a wooden board with lemon"></div>
  </div>

  <div class="panel panel-right paper on-paper">
    <div class="decor" style="left:340px;top:0;width:115px;height:110px;background:var(--blue-soft)" role="img" aria-label="Line-drawn olive branch ornament"></div>
    <div class="decor" style="left:25px;top:40px;width:60px;height:70px;background:var(--blue-pale)" role="img" aria-label="Line drawing of a classical bust"></div>
    <div class="decor" style="left:380px;top:185px;width:70px;height:90px;background:var(--blue-pale)" role="img" aria-label="Line drawing of a fish"></div>
    <div class="decor" style="left:15px;top:325px;width:55px;height:110px;background:var(--blue-pale)" role="img" aria-label="Line drawing of a bottle"></div>
    <div class="decor" style="left:375px;top:555px;width:70px;height:70px;background:var(--blue-pale)" role="img" aria-label="Line drawing of a shrimp"></div>
    <div class="decor" style="left:0;top:590px;width:100px;height:112px;background:var(--blue-soft)" role="img" aria-label="Line-drawn olive branch ornament"></div>

    <div class="abs brand-name">Mi ZOV</div>
    <div class="abs word-food">FOOD</div>
    <div class="abs word-menu">MENU</div>
    <div class="photo" style="left:55px;top:400px;width:370px;height:185px;border-radius:50%;background:radial-gradient(ellipse at 50% 40%,#b5632b 0%,#c98545 45%,#e9e4dd 70%,#f4f4f4 100%)" role="img" aria-label="Photo of a roast chicken on a white platter with lemons, tomatoes and rosemary"></div>
    <div class="abs site">www.mizoveats.com</div>
  </div>
</section>

<section class="spread spread-inside">
  <div class="panel panel-left">
    <div class="abs gold on-gold" style="left:0;top:0;width:454px;height:243px">
      <div class="decor" style="left:300px;top:0;width:130px;height:100px;background:var(--blue)" role="img" aria-label="Line-drawn olive branch ornament"></div>
      <div class="abs heading" style="left:27px;top:28px;--rule:160px">DIPS</div>
      <div class="item" style="left:27px;top:63px;width:193px"><span class="name">Trio Dip Appetizer<span class="note">Tzaziki, Hummus &amp; Tirokafteri served<br>with 2 Pitas</span></span><span class="price">7</span></div>
      <div class="item" style="left:27px;top:113px;width:199px"><span class="name">Tzaziki Dip<span class="note">served w/ 2 pitas</span></span><span class="price">12</span></div>
      <div class="item" style="left:27px;top:155px;width:193px"><span class="name">&nbsp;Tirokafteri Dip<span class="note">served with 2 pitas (spicy feta dip)</span></span><span class="price">8</span></div>
      <div class="item" style="left:27px;top:197px;width:193px"><span class="name">Red Pepper Hummus Dip<span class="note">served w/ 2 pitas</span></span><span class="price">8</span></div>
      <div class="photo" style="left:245px;top:100px;width:195px;height:110px;background:linear-gradient(135deg,#3a3a3a,#f0c14a 45%,#e2b23a 70%,#3a3a3a);transform:rotate(-12deg)" role="img" aria-label="Photo of french fries with dipping sauces on a black board"></div>
    </div>

    <div class="abs paper on-paper" style="left:0;top:243px;width:454px;height:235px">
      <div class="abs heading" style="left:27px;top:30px;--rule:105px">STARTERS</div>
      <div class="item" style="left:27px;top:69px;width:198px"><span class="name">Greek Gigantes Appetizer<span class="note">Large white beans baked in a tomato based<br>sauce topped with feta served w/ pita</span></span><span class="price">10.5</span></div>
      <div class="item" style="left:27px;top:120px;width:195px"><span class="name">Dolmades</span><span class="price">9.5</span></div>
      <div class="item" style="left:27px;top:147px;width:199px"><span class="name">Greek Wings<span class="note">served with 2 pitas (spicy feta dip)</span></span><span class="price">13.5</span></div>
      <div class="item" style="left:27px;top:188px;width:198px"><span class="name">Phyllo Wrapped Feta</span><span class="price">10.9</span></div>

      <div class="abs heading" style="left:274px;top:30px;--rule:110px">FRIES</div>
      <div class="item" style="left:274px;top:69px;width:146px"><span class="name">Seasoned Fries 5<span class="note">Salt, Pepper, Oregano</span></span><span class="price">5</span></div>
      <div class="item" style="left:274px;top:106px;width:146px"><span class="name">Feta Fries- Mi ZOV<span class="note">Seasoned &amp; Feta</span></span><span class="price">5</span></div>
      <div class="item" style="left:274px;top:143px;width:146px"><span class="name">Poutine Fries<span class="note">Kasseri Cheese, Gyro</span></span><span class="price">5</span></div>
      <div class="item" style="left:274px;top:181px;width:146px"><span class="name">Sauce Fries<span class="note">Sauce</span></span><span class="price">5</span></div>
    </div>

    <div class="abs navy on-navy" style="left:0;top:478px;width:454px;height:225px">
      <div class="abs heading" style="left:27px;top:25px;--rule:105px">SALADS</div>
      <div class="abs desc" style="left:27px;top:56px;color:#fff">ZOV: Gyro, Chicken Gyro, Pork Souvlaki<br>or Grilled Shrimp Reg. +6.5/ Lg.+8.5</div>
      <div class="photo" style="left:270px;top:-10px;width:165px;height:75px;background:linear-gradient(180deg,#f4f4f4,#e9c37e 50%,#d7563b 75%,#f4f4f4)" role="img" aria-label="Photo of bruschetta appetizers on a white plate"></div>
      <div class="item" style="left:27px;top:104px;width:185px"><span class="name">Village Salad- Mi ZOV<span class="note">Cherry,tomatoes, cucumbers, Kalamata olives,<br>red onions, green peppers, feta, capers,<br>oregano &amp; Greek Vinaigrette</span></span><span class="price">7</span></div>
      <div class="item" style="left:246px;top:104px;width:180px"><span class="name">Greek Salad-Mi ZOV<span class="note">Romaine mixed green lettuce, tomatoes,<br>cucumbers, onions, olives, pepperoncini,<br>green peppers, Feta &amp; house dressing</span></span><span class="price">7</span></div>
      <div class="item" style="left:27px;top:166px;width:185px"><span class="name">Marouli Salad<span class="note">romaine lettuce, spring onions, dill, cherry<br>tomatoes with kasseri cheese</span></span><span class="price">7</span></div>
      <div class="item" style="left:246px;top:166px;width:180px"><span class="name">Mediterranean Salad<span class="note">mixed green romaine lettuce, cherry<br>tomatoes, olives, dried figs</span></span><span class="price">7</span></div>
    </div>
  </div>

  <div class="panel panel-right paper on-paper">
    <div class="gold-strip"></div>
    <div class="decor" style="left:359px;top:0;width:96px;height:700px;background:var(--gold-deep)" role="img" aria-label="Greek key decorative pattern"></div>
    <div class="decor" style="left:345px;top:0;width:110px;height:105px;background:var(--blue)" role="img" aria-label="Line-drawn olive branch ornament"></div>

    <div class="abs heading" style="left:27px;top:24px;--rule:105px">HANDHELD PITAS</div>
    <div class="abs desc" style="left:27px;top:47px;color:var(--ink)">MIZOV-Tomato, Tzaziki, Red Onions, Fries</div>
    <div class="item" style="left:27px;top:65px;width:224px"><span class="name">Trio Dip Appetizer<span class="note">Tzaziki, Hummus &amp; Tirokafteri served<br>with 2 Pitas</span></span><span class="price">10</span></div>
    <div class="item" style="left:27px;top:110px;width:224px"><span class="name">Tzaziki Dip<span class="note">served w/ 2 pitas</span></span><span class="price">10</span></div>
    <div class="item" style="left:27px;top:146px;width:224px"><span class="name">Tirokafteri Dip<span class="note">served with 2 pitas (spicy feta dip)</span></span><span class="price">10</span></div>
    <div class="item" style="left:27px;top:181px;width:224px"><span class="name">Red Pepper Hummus Dip<span class="note">served w/ 2 pitas</span></span><span class="price">10</span></div>

    <div class="photo" style="left:305px;top:195px;width:145px;height:90px;border-radius:50%;background:radial-gradient(ellipse,#c6874a 0%,#d4533c 40%,#2d2f36 72%)" role="img" aria-label="Photo of a grilled club sandwich on a dark plate"></div>

    <div class="abs heading" style="left:27px;top:230px;--rule:20px">SKEPASTI- ZOV CLUB SANDWICHES</div>
    <div class="abs desc" style="left:27px;top:256px;color:var(--ink)">MIZOV Skepasti- served on pita w/ lettuce,<br>tomatoes, red onions &amp; ZOV mafia sauce</div>
    <div class="item" style="left:27px;top:288px;width:224px"><span class="name">MIZOV- Gyro Club</span><span class="price">12</span></div>
    <div class="item" style="left:27px;top:308px;width:224px"><span class="name">MIZOV- Pork Belly Club</span><span class="price">12</span></div>
    <div class="item" style="left:27px;top:329px;width:224px"><span class="name">MIZOV- Grilled Chicken Club</span><span class="price">12</span></div>

    <div class="abs heading" style="left:27px;top:362px;--rule:105px">MI ZOV BOWLS</div>
    <div class="abs desc" style="left:27px;top:390px;color:var(--ink)">Mi ZOV: Rice, mixed greens or romaine, tomatoes, cucumbers,<br>red onions, feta, kalamata olives &amp; a scoop of tzatziki &amp;<br>tirokafteri (spicy feta) w/ Greek vinaigrette $12.5</div>
    <div class="item" style="left:27px;top:434px;width:230px"><span class="name">Mi ZOV Add Gyro</span><span class="price">14.9</span></div>
    <div class="item" style="left:27px;top:454px;width:230px"><span class="name">Add Grilled Chicken</span><span class="price">15.9</span></div>
    <div class="item" style="left:27px;top:474px;width:230px"><span class="name">Add Pork Belly</span><span class="price">17.5</span></div>
    <div class="item" style="left:27px;top:494px;width:230px"><span class="name">Add Salmon</span><span class="price">17.5</span></div>

    <div class="photo" style="left:330px;top:420px;width:125px;height:105px;border-radius:50%;background:radial-gradient(ellipse,#c63a22 0%,#eab25a 35%,#f2f2f2 70%)" role="img" aria-label="Photo of a bowl of hummus with paprika"></div>

    <div class="abs heading" style="left:27px;top:535px;--rule:105px">ENTRÉES</div>
    <div class="item" style="left:27px;top:567px;width:224px"><span class="name">MIZOV- Gyro Platter<span class="note">MIZOV- Served with Pita, Tzaziki, Rice &amp; Salad</span></span><span class="price">12</span></div>
    <div class="item" style="left:27px;top:597px;width:224px"><span class="name">MIZOV- Pork Souvlaki Platter<span class="note">MIZOV- Served with Pita, Tzaziki, Rice &amp; Salad</span></span><span class="price">12</span></div>
    <div class="item" style="left:27px;top:628px;width:224px"><span class="name">MIZOV- Chicken Platter<span class="note">MIZOV- Served with Pita, Tzaziki, Rice &amp; Salad</span></span><span class="price">12</span></div>
    <div class="item" style="left:27px;top:659px;width:224px"><span class="name">MIZOV- Falalfal Platter<span class="note">MIZOV- Served with Pita, Tzaziki, Rice &amp; Salad</span></span><span class="price">12</span></div>

    <div class="photo" style="left:310px;top:575px;width:145px;height:100px;border-radius:50%;background:radial-gradient(ellipse,#1f1f22 0%,#f08a5d 38%,#f2f2f2 68%)" role="img" aria-label="Photo of salmon with black pasta on a white plate"></div>
  </div>
</section>

</body>
</html>
```